ROVA Pty Ltd Business Card

Looking for a simple yet eye-catching double-sided business card design using my company logo on one side and contact details on the other.

Target Market(s)

Government

Industry/Entity Type

Communication Systems Engineering

Contact Information for Business Card

ROVA Pty Ltd

Requirements
Nice to have
• Would be great to have a QR code so details can be scanned into contacts

```html
<!DOCTYPE html>
<html lang="en">
<head>
<meta charset="utf-8">
<title>ROVA Pty Ltd Business Card</title>
<link href="https://fonts.googleapis.com/css2?family=Montserrat:wght@400;700&display=swap" rel="stylesheet">
<style>
  :root {
    --backdrop: #d9d8d5;
    --card: #ffffff;
    --slate: #37424a;
    --ink: #0e0e0e;
    --text: #2b3238;
  }
  * { margin: 0; padding: 0; box-sizing: border-box; }
  html, body { width: 1200px; height: 801px; overflow: hidden; }
  body {
    background: var(--backdrop);
    font-family: "Montserrat", sans-serif;
    color: var(--text);
    position: relative;
  }
  .card {
    position: absolute;
    top: 250px;
    width: 525px;
    height: 300px;
    background: var(--card);
    border-radius: 18px;
    overflow: hidden;
    box-shadow: 0 10px 24px rgba(0,0,0,0.18);
  }
  .card--front { left: 50px; }
  .card--back { left: 625px; }

  .brand {
    position: absolute;
    display: flex;
    align-items: center;
    gap: 14px;
  }
  .brand__mark {
    border-radius: 50%;
    background: var(--slate);
  }
  .brand__name {
    font-weight: 700;
    color: var(--slate);
    letter-spacing: 0.04em;
    line-height: 1;
  }
  .card--front .brand { left: 38px; top: 112px; }
  .card--front .brand__mark { width: 30px; height: 30px; }
  .card--front .brand__name { font-size: 46px; }

  .card--back .brand { left: 50%; top: 50%; transform: translate(-50%, -50%); gap: 22px; }
  .card--back .brand__mark { width: 52px; height: 52px; }
  .card--back .brand__name { font-size: 84px; }

  .divider {
    position: absolute;
    left: 262px;
    top: 42px;
    width: 1px;
    height: 182px;
    background: var(--slate);
  }
  .contact {
    position: absolute;
    left: 280px;
    top: 42px;
    width: 230px;
  }
  .contact__name {
    font-weight: 700;
    font-size: 19px;
    letter-spacing: 0.02em;
    color: var(--slate);
    line-height: 1.1;
  }
  .contact__role {
    font-size: 12.5px;
    margin-top: 3px;
  }
  .contact__list {
    list-style: none;
    margin-top: 16px;
    font-size: 12.5px;
    line-height: 1.55;
  }
  .contact__list li { display: flex; align-items: center; gap: 7px; }
  .contact__list svg { width: 11px; height: 11px; fill: var(--slate); flex: none; }
  .contact__address {
    font-size: 12.5px;
    line-height: 1.45;
    margin-top: 14px;
  }
  .edge-band {
    position: absolute;
    left: 0;
    bottom: 0;
    width: 525px;
    height: 40px;
  }
</style>
</head>
<body>

  <section class="card card--front" aria-label="Business card, contact side">
    <div class="brand">
      <span class="brand__mark"></span>
      <span class="brand__name">ROVA</span>
    </div>

    <div class="divider"></div>

    <div class="contact">
      <p class="contact__name">DANIEL HARPER</p>
      <p class="contact__role">Managing Director</p>
      <ul class="contact__list">
        <li>
          <svg viewBox="0 0 24 24" aria-hidden="true"><path d="M6.6 10.8a15.1 15.1 0 0 0 6.6 6.6l2.2-2.2a1 1 0 0 1 1-.25 11.4 11.4 0 0 0 3.6.57 1 1 0 0 1 1 1V20a1 1 0 0 1-1 1A17 17 0 0 1 3 4a1 1 0 0 1 1-1h3.5a1 1 0 0 1 1 1c0 1.25.2 2.45.57 3.57a1 1 0 0 1-.25 1z"/></svg>
          987 654 321
        </li>
        <li>
          <svg viewBox="0 0 24 24" aria-hidden="true"><path d="M2 5h20v14H2zm2 2v.4l8 5 8-5V7z"/></svg>
          admin@rova.com.au
        </li>
        <li>
          <svg viewBox="0 0 24 24" aria-hidden="true"><circle cx="12" cy="12" r="10"/></svg>
          www.rova.com.au
        </li>
      </ul>
      <p class="contact__address">42-44 Wattle Road Kellyvale<br>NSW 2150 Australia</p>
    </div>

    <svg class="edge-band" viewBox="0 0 525 40" preserveAspectRatio="none" aria-hidden="true">
      <polygon points="0,28 290,28 290,31 0,31" fill="var(--ink)"/>
      <polygon points="0,34 290,34 296,10 525,10 525,40 0,40" fill="var(--slate)"/>
    </svg>
  </section>

  <section class="card card--back" aria-label="Business card, logo side">
    <div class="brand">
      <span class="brand__mark"></span>
      <span class="brand__name">ROVA</span>
    </div>
  </section>

</body>
</html>
```